New signage for apartment community in the Pacific Northwest

Signage for an apartment community in the Pacific Northwest. It should have a contemporary northwest vibe with a fresh exciting feeling. We are open to the colors cayenne, white, charcoal and a splash of lime green. Sign to have the name 'VELTO' with the address number 28391 smaller underneath. sign can include a shape under the name or a feeling of energy in the shape of the name.

Target Market(s)

Young urban professionals

Industry/Entity Type

Real Estate Development

Requirements
Must have
• eyecatching
Should not have
• anything too cute or too busy

```html
<!DOCTYPE html>
<html lang="en">
<head>
<meta charset="utf-8">
<title>VELTO 28391 – Community Sign</title>
<link rel="stylesheet" href="https://fonts.googleapis.com/css2?family=Sorts+Mill+Goudy:ital@0;1&family=Montserrat:wght@500&display=swap">
<style>
  :root {
    --forest-charcoal: #2f3d3a;
    --forest-charcoal-deep: #25322f;
    --lime: #a9c93a;
    --lime-olive: #6e8a35;
    --panel-light: #ebebeb;
    --panel-lighter: #f2f2f2;
    --name-white: #eef1f1;
    --name-mist: #c9d3d2;
    --ink: #27302e;
  }
  html, body {
    margin: 0;
    padding: 0;
    width: 1200px;
    height: 884px;
    overflow: hidden;
    background: var(--panel-light);
  }
  .sign {
    display: block;
    width: 1200px;
    height: 884px;
  }
  .sign__name {
    font-family: "Sorts Mill Goudy", "Goudy Old Style", serif;
    font-size: 200px;
    fill: var(--name-white);
  }
  .sign__number {
    font-family: "Montserrat", sans-serif;
    font-weight: 500;
    font-size: 60px;
    fill: var(--lime);
  }
  .sign__slogan {
    font-family: "Sorts Mill Goudy", "Goudy Old Style", serif;
    font-style: italic;
    font-size: 60px;
    fill: var(--ink);
  }
  .sign__frame {
    fill: none;
    stroke: var(--lime);
    stroke-width: 1.5;
  }
</style>
</head>
<body>
<svg class="sign" viewBox="0 0 1200 884" xmlns="http://www.w3.org/2000/svg">
  <defs>
    <linearGradient id="lowerPanel" x1="0" y1="0" x2="0" y2="1">
      <stop offset="0" stop-color="var(--panel-lighter)"/>
      <stop offset="1" stop-color="var(--panel-light)"/>
    </linearGradient>
    <linearGradient id="skylineStrip" x1="0" y1="0" x2="0" y2="1">
      <stop offset="0" stop-color="#c9cccb"/>
      <stop offset="1" stop-color="#e2e4e3"/>
    </linearGradient>
    <linearGradient id="chevronBand" x1="0" y1="0" x2="1" y2="0">
      <stop offset="0" stop-color="var(--lime-olive)"/>
      <stop offset="0.5" stop-color="var(--lime)"/>
      <stop offset="1" stop-color="var(--lime-olive)"/>
    </linearGradient>
    <linearGradient id="buildingsPanel" x1="0" y1="0" x2="0" y2="1">
      <stop offset="0" stop-color="var(--forest-charcoal-deep)"/>
      <stop offset="1" stop-color="var(--forest-charcoal)"/>
    </linearGradient>
  </defs>

  <rect class="sign__lower" width="1200" height="884" fill="url(#lowerPanel)"/>

  <polygon class="sign__skyline-strip" role="img" aria-label="Photo strip of apartment towers"
           points="0,463 1200,463 600,690" fill="url(#skylineStrip)"/>

  <polygon class="sign__chevron" points="70,478 600,630 1130,478 600,664" fill="url(#chevronBand)"/>

  <polygon class="sign__hero" role="img" aria-label="Photograph of modern apartment towers toned in dark forest green"
           points="0,0 1200,0 1200,463 600,605 0,463" fill="url(#buildingsPanel)"/>

  <polyline class="sign__frame" points="712,407 224,407 224,128 976,128 976,407 899,407"/>

  <text class="sign__name" x="274" y="349" textLength="620" lengthAdjust="spacingAndGlyphs">VELTO</text>

  <text class="sign__number" x="806" y="428" text-anchor="middle">28391</text>

  <text class="sign__slogan" x="600" y="802" text-anchor="middle">Some slogan to come</text>
</svg>
</body>
</html>
```